Label Design For "TUB HALO". All natural liquid water treatment for hot tubs & spas.

Launching a new all natural product to the spa & hot tub market. It's an enzyme based liquid that will come in an aluminum bottle, roughly 500ml.
Allows the user to use far less harsh chemicals in their hot tub while making the water softer and smoother on your skin.

Product is called TUB HALO. The reason for the name is that it uses zero chemicals, zero waste, zero animal testing, and zero effort to use it in your hot tub care routine.

There is no logo, icon, or font. Please feel free to use creative freedom with fonts. Looking for a bold, clean, minimal font for the name, preferably sans serif. A modern bold look that's really clean and minimal is what I'm looking for. The name itself will most likely be the logo. Feel free to spell the word zero or use the number 0 instead in the name.

All of our competition uses a white plastic bottle with a navy blue label. I would like to look completely different from them on a shelf. Something that implies it's natural and soft, and not old, clinical, and industrial.

These are eco friendly products with eco friendly packaging, but I don't want to use green or blue in the colours. Im obviously not a designer at all so please let your ideas flow. I like pastels or bold colours, even black and white. If you have better ideas, I'm open to suggestion. I have attached a couple images that show what my competition looks like and also some design looks and colours I like.

Target Market(s)

Spa & hot tub owners that use their own chemicals weekly/monthly - 80% Male / 20% Female

Industry/Entity Type

Hot Tub Chemicals & Water Care

Font styles to use
Sans Serif

Requirements
Must have
• Clean, Minimal, Modern. Sans Serif Font. The name "TUB HALO". Mention that it's all natural, eco friendly water conditioner for hot tubs and spas.
Nice to have
• Multiple mockups with different colour pallets
Should not have
• Please not busy looking, and please no use of blue or green.

```html
<!DOCTYPE html>
<html lang="en">
<head>
<meta charset="utf-8">
<title>TUB HALO – Label Colourways</title>
<link rel="stylesheet" href="https://fonts.googleapis.com/css2?family=Fira+Sans:wght@400;500&family=Amatic+SC:wght@400;700&display=swap">
<style>
  :root {
    --page: #f2f0ee;
    --white: #ffffff;
  }
  * { box-sizing: border-box; margin: 0; padding: 0; }
  html, body {
    width: 1200px; height: 1200px; overflow: hidden;
    background: var(--page);
  }
  .canvas {
    position: relative; width: 1200px; height: 1200px;
    display: flex; justify-content: center; align-items: center; gap: 60px;
  }
  .label {
    position: relative; width: 405px; height: 1000px; overflow: hidden;
    background: var(--bg);
    font-family: "Fira Sans", sans-serif;
    color: var(--ink);
  }
  .label--terracotta {
    --bg: #dac8a8;
    --tone-soft: #efb08a;
    --ink: #b5583a;
    --ink-deep: #9e4a30;
  }
  .label--rose {
    --bg: #d7c3c1;
    --tone-soft: #e48f9c;
    --ink: #b24a84;
    --ink-deep: #9a3d72;
  }
  .label__backdrop {
    position: absolute; inset: 0;
    background: linear-gradient(165deg,
      var(--tone-soft) 0%,
      var(--bg) 28%,
      var(--bg) 62%,
      var(--ink) 100%);
  }
  .label__descriptor {
    position: absolute; left: 18px; top: 38px;
    font-size: 17.5px; font-weight: 400; letter-spacing: 0.1px;
    white-space: nowrap;
    color: var(--ink-deep);
  }
  .label__name {
    position: absolute; left: 40px; top: 250px; width: 330px;
    font-family: "Fira Sans", sans-serif; font-weight: 500;
    font-size: 118px; line-height: 1.0; letter-spacing: 2px;
    color: var(--ink);
  }
  .label__name-mark {
    position: absolute; left: 278px; top: 182px;
    width: 40px; height: 40px; border-radius: 50%;
    border: 3px solid var(--ink);
  }
  .label__tagline {
    position: absolute; left: 0; right: 0; top: 652px;
    font-family: "Amatic SC", sans-serif; font-weight: 400;
    font-size: 22px; text-align: center; white-space: nowrap;
    color: #5d4a40;
    transform: rotate(-2.5deg);
  }
  .label--rose .label__tagline { color: var(--ink); }
  .badge { position: absolute; border-radius: 50%; }
  .badge--chemicals { left: 20px; top: 730px; width: 64px; height: 110px; border-radius: 40%; background: linear-gradient(#b7c98a, #b9997a); }
  .badge--eco { left: 148px; top: 740px; width: 128px; height: 130px; border-radius: 45%; background: linear-gradient(#7fc07a, #e47f86); }
  .badge--waste { left: 293px; top: 757px; width: 94px; height: 94px; background: linear-gradient(#f08a8a, #7fc07a); }
  .badge--animals { left: 72px; top: 850px; width: 94px; height: 102px; border-radius: 40%; background: linear-gradient(var(--white), #a9cf9a); }
  .label__cruelty {
    position: absolute; left: 70px; top: 956px; width: 100px;
    font-family: "Amatic SC", sans-serif; font-size: 11px; text-align: center;
    white-space: nowrap; color: #6b5a4a;
  }
  .label__volume {
    position: absolute; right: 16px; bottom: 38px;
    font-size: 19px; color: var(--white); letter-spacing: 0.3px;
    white-space: nowrap;
  }
</style>
</head>
<body>
<main class="canvas">

  <section class="label label--terracotta">
    <div class="label__backdrop" role="img" aria-label="Soft organic colour-blob background in peach, blush and terracotta"></div>
    <p class="label__descriptor">water conditioner for hot tubs and spas</p>
    <span class="label__name-mark"></span>
    <h1 class="label__name">TUB<br>HALO</h1>
    <p class="label__tagline">Zero effort to use it in your hot tub care routine</p>
    <div class="badge badge--chemicals" role="img" aria-label="Zero chemicals badge: seedling held in hands"></div>
    <div class="badge badge--eco" role="img" aria-label="Eco friendly badge: tree with ribbon"></div>
    <div class="badge badge--waste" role="img" aria-label="Zero waste badge: globe with flowers"></div>
    <div class="badge badge--animals" role="img" aria-label="Not tested on animals badge: rabbit with carrot"></div>
    <p class="label__cruelty">NOT TESTED ON ANIMALS</p>
    <p class="label__volume">500ml/16 Oz</p>
  </section>

  <section class="label label--rose">
    <div class="label__backdrop" role="img" aria-label="Soft organic colour-blob background in rose, pink and magenta"></div>
    <p class="label__descriptor">water conditioner for hot tubs and spas</p>
    <span class="label__name-mark"></span>
    <h1 class="label__name">TUB<br>HALO</h1>
    <p class="label__tagline">Zero effort to use it in your hot tub care routine</p>
    <div class="badge badge--chemicals" role="img" aria-label="Zero chemicals badge: seedling held in hands"></div>
    <div class="badge badge--eco" role="img" aria-label="Eco friendly badge: tree with ribbon"></div>
    <div class="badge badge--waste" role="img" aria-label="Zero waste badge: globe with flowers"></div>
    <div class="badge badge--animals" role="img" aria-label="Not tested on animals badge: rabbit with carrot"></div>
    <p class="label__cruelty">NOT TESTED ON ANIMALS</p>
    <p class="label__volume">500ml/16 Oz</p>
  </section>

</main>
</body>
</html>
```